K7T Business Cards

I need a very sleek design using the logo attached. I want something very simple and clean, yet still creative. On the black I would like some sort of matte black finish, so make the design that will fit that accordingly.

I have attached the information needed in the card with the logo image.

Business

```html
<!DOCTYPE html>
<html lang="en">
<head>
<meta charset="utf-8">
<title>K7T Business Cards</title>
<link href="https://fonts.googleapis.com/css2?family=PT+Serif:wght@400;700&display=swap" rel="stylesheet">
<style>
  :root {
    --backdrop: #f6f8f7;
    --card-black-top: #050505;
    --card-black-bottom: #3a3a38;
    --card-matte: #171c1b;
    --accent-orange: #f7931e;
    --accent-white: #ffffff;
    --brand-blue: #1a7fd0;
    --text-white: #ffffff;
    --text-sage: #62805e;
    --rule-grey: #8a8f8c;
  }
  * { margin: 0; padding: 0; box-sizing: border-box; }
  html, body {
    width: 1200px;
    height: 1000px;
    overflow: hidden;
    background: var(--backdrop);
    font-family: "PT Serif", Georgia, serif;
  }
  .canvas {
    position: relative;
    width: 1200px;
    height: 1000px;
  }
  .card {
    position: absolute;
    top: 404px;
    width: 323px;
    height: 202px;
    overflow: hidden;
    border-radius: 14px 0 14px 0;
  }
  .card-front {
    left: 270px;
    background: linear-gradient(to bottom, var(--card-black-top) 0%, var(--card-black-top) 38%, var(--card-black-bottom) 100%);
  }
  .card-back {
    left: 626px;
    background: var(--card-matte);
  }
  .front-swoosh {
    position: absolute;
    inset: 0;
  }
  .brand-divider {
    position: absolute;
    left: 109px;
    top: 0;
    width: 1px;
    height: 84px;
    background: var(--accent-white);
  }
  .brand-mark {
    position: absolute;
    left: 22px;
    top: 22px;
    width: 20px;
    height: 20px;
    background: var(--brand-blue);
  }
  .brand-name {
    position: absolute;
    left: 122px;
    top: 22px;
    width: 150px;
    color: var(--brand-blue);
    font-weight: 700;
    font-size: 16px;
    line-height: 17px;
    letter-spacing: 1px;
  }
  .holder-name {
    position: absolute;
    left: 17px;
    top: 100px;
    color: var(--text-white);
    font-size: 24px;
    line-height: 28px;
  }
  .holder-title {
    position: absolute;
    left: 17px;
    width: 173px;
    top: 130px;
    text-align: right;
    color: var(--text-white);
    font-size: 12px;
    line-height: 14px;
  }
  .contact-rule {
    position: absolute;
    left: 47px;
    width: 231px;
    height: 1px;
    background: var(--rule-grey);
  }
  .contact-rule.top { top: 54px; }
  .contact-rule.bottom { top: 136px; }
  .contact-list {
    position: absolute;
    left: 0;
    right: 0;
    top: 61px;
    list-style: none;
    text-align: center;
    color: var(--text-sage);
    font-size: 17px;
    line-height: 23px;
  }
</style>
</head>
<body>
  <main class="canvas">
    <section class="card card-front" aria-label="Business card front">
      <svg class="front-swoosh" width="323" height="202" viewBox="0 0 323 202" aria-hidden="true">
        <path d="M0 202 C 120 196, 260 150, 323 46 L 323 68 C 270 160, 140 200, 0 202 Z" fill="var(--accent-white)"/>
        <path d="M0 202 C 140 200, 270 160, 323 68 L 323 202 Z" fill="var(--accent-orange)"/>
      </svg>
      <span class="brand-mark" aria-hidden="true"></span>
      <span class="brand-divider" aria-hidden="true"></span>
      <div class="brand-name">KESTREL 7 TRADING</div>
      <h1 class="holder-name">Owen Hartley</h1>
      <p class="holder-title">Sales Executive</p>
    </section>

    <section class="card card-back" aria-label="Business card back">
      <span class="contact-rule top" aria-hidden="true"></span>
      <ul class="contact-list">
        <li>Email: owen@k7t.net</li>
        <li>Website: www.k7t.net</li>
        <li>Phone: 555.014.0273</li>
      </ul>
      <span class="contact-rule bottom" aria-hidden="true"></span>
    </section>
  </main>
</body>
</html>
```